We have a parent company, Summit Harbor Group (SHG), that has other company partners. We are looking for ways to incorporate our SHG logo with our network partners, Beacon Ledger and The Blue Gate. My initial thought is to have SHG as front of card logo, and include The Blue Gate and Beacon Ledger logos on back but I'm open to ideas. Card should include website www.summitharborgrp.example (use for reference). Keywords "Tax Services" "Real Estate" "Insurance" "Investments" "Chief Financial Officer"

Industry/Entity Type

Financial

```html
<!DOCTYPE html>
<html lang="en">
<head>
<meta charset="utf-8">
<title>Summit Harbor Group — Business Card</title>
<link rel="stylesheet" href="https://fonts.googleapis.com/css2?family=Open+Sans:wght@400;600;700&display=swap">
<style>
  :root {
    --backdrop: #73685a;
    --card: #ffffff;
    --brand-blue: #1c4ea2;
    --brand-red: #e81f2d;
    --ink: #231f20;
    --partner-wine: #7a1f3d;
    --icon-tint: #f7d9dc;
  }
  * { margin: 0; padding: 0; box-sizing: border-box; }
  html, body { width: 1200px; height: 1200px; overflow: hidden; }
  body {
    background: var(--backdrop);
    font-family: "Open Sans", Arial, sans-serif;
    color: var(--ink);
    position: relative;
  }
  .card {
    position: absolute;
    left: 288px;
    width: 629px;
    height: 359px;
    background: var(--card);
    overflow: hidden;
  }
  .card--front { top: 214px; }
  .card--back { top: 670px; }

  /* Front */
  .brand {
    position: absolute;
    left: 0; right: 0;
    top: 78px;
    display: flex;
    flex-direction: column;
    align-items: center;
  }
  .brand__mark {
    width: 92px; height: 92px;
    border-radius: 50%;
    background: var(--brand-red);
  }
  .brand__name {
    margin-top: 14px;
    font-size: 31px;
    line-height: 1.1;
    font-weight: 600;
    color: var(--brand-blue);
    letter-spacing: 0.5px;
  }
  .website {
    position: absolute;
    left: 29px;
    top: 318px;
    font-size: 15px;
    letter-spacing: 0.2px;
  }
  .partners {
    position: absolute;
    right: 26px;
    top: 314px;
    display: flex;
    align-items: center;
    gap: 8px;
    font-size: 16px;
    font-weight: 700;
  }
  .partners__item--ledger { color: var(--brand-red); }
  .partners__item--gate { color: var(--partner-wine); }
  .partners__divider {
    width: 1px; height: 20px;
    background: #b9b9b9;
  }

  /* Back */
  .person {
    position: absolute;
    left: 77px;
    top: 150px;
  }
  .person__name {
    font-size: 32px;
    line-height: 1;
    letter-spacing: -0.5px;
  }
  .person__name strong { font-weight: 700; }
  .person__name span { font-weight: 400; }
  .person__title {
    margin-top: 6px;
    font-size: 18px;
    font-weight: 400;
  }
  .contact {
    position: absolute;
    left: 334px;
    top: 100px;
    list-style: none;
  }
  .contact__row {
    display: flex;
    align-items: center;
    margin-bottom: 14px;
  }
  .contact__icon {
    width: 32px; height: 32px;
    margin-right: 31px;
    flex: none;
  }
  .contact__icon svg { width: 32px; height: 32px; fill: var(--icon-tint); }
  .contact__lines {
    font-size: 15px;
    line-height: 21px;
    white-space: nowrap;
  }
  .services {
    position: absolute;
    left: 0; right: 0;
    top: 326px;
    height: 17px;
    background: var(--brand-red);
    color: #fff;
    font-size: 12px;
    line-height: 17px;
    letter-spacing: 2.4px;
    text-align: center;
    word-spacing: 2px;
  }
</style>
</head>
<body>

<section class="card card--front">
  <div class="brand">
    <span class="brand__mark"></span>
    <span class="brand__name">Summit Harbor Group</span>
  </div>
  <p class="website">WWW.SUMMITHARBORGRP.EXAMPLE</p>
  <div class="partners">
    <span class="partners__item partners__item--ledger">BEACON LEDGER</span>
    <span class="partners__divider"></span>
    <span class="partners__item partners__item--gate">The Blue Gate</span>
  </div>
</section>

<section class="card card--back">
  <div class="person">
    <h1 class="person__name"><strong>JOHN</strong> <span>DOE</span></h1>
    <p class="person__title">DESIGNATION</p>
  </div>

  <ul class="contact">
    <li class="contact__row">
      <span class="contact__icon">
        <svg viewBox="0 0 32 32" aria-hidden="true"><path d="M7 3c1.2 0 4.5 5.5 4.5 6.8S9 12.5 9 13.5c0 2 7.5 9.5 9.5 9.5 1 0 2.4-2.5 3.7-2.5S29 23.8 29 25c0 1.5-3.2 4-5 4C14 29 3 18 3 8c0-1.8 2.5-5 4-5z"/></svg>
      </span>
      <div class="contact__lines">555.010.2040<br>555.010.2040</div>
    </li>
    <li class="contact__row">
      <span class="contact__icon">
        <svg viewBox="0 0 32 32" aria-hidden="true"><path d="M2 7h28v18H2z M4 9v1l12 8 12-8V9l-12 8z" fill-rule="evenodd"/></svg>
      </span>
      <div class="contact__lines">info@company.com<br>name@company.com</div>
    </li>
    <li class="contact__row">
      <span class="contact__icon">
        <svg viewBox="0 0 32 32" aria-hidden="true"><path d="M16 3 2 15h4v12h8v-8h4v8h8V15h4z M2 29h28v2H2z"/></svg>
      </span>
      <div class="contact__lines">2417 Harbor Ridge Rd<br>Lakeview, CO 80990</div>
    </li>
  </ul>

  <p class="services">TAX SERVICES | REAL ESTATE | INSURANCE | INVESTMENTS</p>
</section>

</body>
</html>
```